Full revamp of cheap website design - the best designer will be offered a much larger project!

Tolland Vesper are a progressive and innovative mid-tier professional services group (accountants and business advisors) with offices based in major cities throughout Australia and New Zealand.
Our positioning statement is "Energetic, Innovative, Streetwise", and the visual appearance must reflect this. Although still a relatively conservative industry, we aim to project a modern, innovative, energetic, highly professional but approachable image. The presentation should tie in with the theme "we take our work seriously, not ourselves".
Our aim with this new design is the elevate the status of the group in its online presentation and communication... we want to 'impress' and stand out from the crowd! See our existing site at www.tollandvesper.com.au
We're looking for a special designer to take on the Web Site Design Concept - Uncoded - graphics only in line with the concept architecture we will provide (although we are flexible with the layout - we want an interface design that works!). Must work within the constraints of a suitable wordpress theme... Designer to source (we quite like themoquill.com as an option, but havn't seen any really slick representations of it)... there are many other great themes to choose from). Must include a series of slick flash banner designs.
or alternatively,
Design and coding (custom design theme) using wordpress platform (unless you can convince us of the benefits of using some other recognised and supported platform).
Happy to receive the design concepts as graphics only (but the flash is an important factor). You'll need to prove that it will work within an existing theme (or that you are capable of quickly developing a bug-free custom site on the wordpress platform.
Only highly talented and professional designers need enter, but the right designer will be well rewarded with the offer of a much larger design project and plenty of ongoing work.
Task
We are completely overhauling our existing and outdated website(s) x 9 and are looking for a new visual design concept (homepage plus one inside section homepage, one information page and one state homepage to start).
Once our executive have selected and approved the winning concept, we will offer you the opportunity to complete all other sections of the site including a variety of flash banners and other visual section headings, advertising and promotional pieces not only for the central tollandvesper.com.au site, but for all of the state sites (8), which will replicate the central site with mainly banner and advertising changes. We will look after content entry.
This project will grow into quite a large opportunity for the right designer with ongoing design elements in the form of flash banners, banner ads, newsletter and other emarketing designs, plus related blogs and product sites required over time.
We will provide you with a flexible wireframe architecture from which to work, along with conceptual content and imagery where available (feel free to use stock images wherever necessary). If you need something else, just ask!
Deadline
Unfortunately, we need you to work to a ridiculously tight deadline on the concept design, due to a pending executive meeting (where we are committed to making a decision on the approved concept). We need your designs to be submitted by 3/11/2009. The good news is that we can get started on the full project reasonably quickly following the first deadline.
Some of our competitors:
www.bellcastrow.com.au
www.lunden.com.au
www.quillam.com.au
www.zrt.com.au
www.vne.com.au
www.oscarmeade.com.au
www.tavro.com.au
www.pellingtrust.com.au
www.gzt.com.au
www.dorvi.com
You'll need to contact me at marenb@tollandvesper.net so that I can give you access to the resources you'll need to get the conceptual design job done. Just send me a quick note letting me know that you're interested in the contest.
Updates
Hello to all Tolland Vesper website redesign competitors!
A quick hello to all our competitors!
Thank you for submitting your fabulous designs... I will be looking at each of them tomorrow (PM) and will provide you with individual feedback and in some cases, requests for minor modifications prior to our Executive presentation on the 6th. Once again, I do apologise for the delay in my response and the rush required at your end.
Many thanks
Maren
Hello,
I have extended the deadline via ArtQuarry to enable you to make the requested changes and get them back to me asap TODAY!
Although I only extended the deadline by 1 day, it is now showing as almost 2 days left. This is not the case. I MUST have your revised designs as soon as possible TODAY.
Many thanks for your great work!
Maren
Hi!
Hello Art Quarry Contestants!
I'm terribly sorry about the delay... still waiting on the OK from our Senior Executive members on which design we will pursue. I am chasing an answer and will get back to you as soon as possible.
Many thanks for your patience.
Maren
Target Market(s)
Our primary target is the mid-size SME marketplace with turnover $5 - $50mil (CFO, COO, MD, GM - ie, Senior Executives) plus High Net worth individuals and high quality staff.
Tolland Vesper's target market are clients who have (and are) invested in their businesses and/or themselves but now need our assistance to grow and develop further.
They need accountants and advisers who can deliver more than the fundamentals. Our clients are defined by an attitude that motivates them to seek out opportunities while putting the structures in place to ensure the security of their futures.
Number of Pages Required
4 pages
Requirements
Must have
- Designs must be clean and uncluttered whilst maintaining a slick and professional yet approachable look and feel.
The corporate logo must be used and unchanged.
A series of attractive, text based flash animated banners will be required to highlight our key messaging
All of the page components as outlined in the concept design provided are required (although layout and other suggested modifications are welcomed).
As noted earlier, you need to contact me at marenb@tollandvesper.net so that I can give you access to the resources you''ll need to get the conceptual design job done. Just send me a quick note letting me know that you''re interested in the content.
Nice to have
- If possible (although not absolutely necessary), consideration should be made regarding tying in our NZ member firm''s site design at www.tollandvesper.co.nz (which will not change) along with www.caldrewglobal.com. Although we don''t wish to replicate either of these designs, it would be nice to somehow connect them visually in some way. Certainly the site map at the bottom of the page (like the NZ site) must be maintained.
If you want to chat through the brief you are welcome to call or IM me on skype: maren.belitsos
Should not have
- images of abacus''s!

```html
<!DOCTYPE html>
<html lang="en">
<head>
<meta charset="utf-8">
<title>Tolland Vesper – Website Concept</title>
<link href="https://fonts.googleapis.com/css2?family=Arimo:wght@400;700&display=swap" rel="stylesheet">
<style>
:root{
  --stage:#6f6f6f;
  --white:#ffffff;
  --ink:#111111;
  --body:#666666;
  --brand:#0098d8;
  --banner-top:#0aa6e4;
  --banner-bottom:#0088c9;
  --banner-line:#7fd0f1;
  --accent:#fff200;
  --panel:#f5f5f5;
  --footer:#000000;
  --footer-text:#d6d6d6;
  --rss:#f26f21;
}
*{margin:0;padding:0;box-sizing:border-box}
html,body{width:1200px;height:3129px;overflow:hidden}
body{background:var(--stage);font-family:"Arimo",Arial,sans-serif;color:var(--body);position:relative}
.page{position:absolute;left:45px;width:1110px;height:1496px;background:var(--white);overflow:hidden}
.page--home{top:45px}
.page--inner{top:1586px}

/* header */
.masthead{position:absolute;left:0;top:0;width:100%;height:108px}
.brand{position:absolute;left:127px;top:36px;display:flex;align-items:center;gap:12px}
.brand__dot{width:40px;height:40px;border-radius:50%;background:var(--brand)}
.brand__name{font-size:30px;font-weight:700;color:var(--ink);letter-spacing:-.5px}
.mainnav{position:absolute;left:0;top:108px;width:100%;height:34px;background:var(--footer)}
.mainnav ul{list-style:none}
.mainnav li{position:absolute;top:12px;font-size:9px;font-weight:700;color:var(--white);letter-spacing:.8px;text-transform:uppercase}
.mainnav li.is-current{top:7px;left:127px;width:65px;height:38px;background:var(--white);color:var(--ink);text-align:center;padding-top:5px;z-index:3}

/* banners */
.hero{position:absolute;left:0;top:142px;width:100%;background:linear-gradient(var(--banner-top),var(--banner-bottom));border-bottom:4px solid var(--banner-line);color:var(--white)}
.hero--home{height:294px}
.hero--inner{height:196px}
.hero__title{position:absolute;font-weight:700;letter-spacing:-.5px;line-height:1;white-space:nowrap}
.hero--home .hero__title{left:130px;top:58px;font-size:46px}
.hero__num{color:var(--accent)}
.hero__lead{position:absolute;font-weight:700;white-space:nowrap}
.hero--home .hero__lead{left:163px;top:116px;font-size:19px;line-height:21px}
.hero__body{position:absolute;left:163px;top:182px;width:530px;font-size:11px;font-weight:700;line-height:14px}
.hero__photo{position:absolute;right:0;top:0;width:290px;height:290px;background:linear-gradient(135deg,#d9dde1,#8d9399 60%,#2b2d31)}
.hero--inner .hero__title{left:125px;top:44px;font-size:48px}
.hero--inner .hero__lead{left:125px;top:101px;font-size:19.5px;line-height:22px}
.pager{position:absolute;display:flex;gap:2px;font-size:10px;font-weight:700;color:var(--ink);line-height:1}
.pager span{display:block;width:11px;text-align:center;padding-top:4px}
.pager span.is-current{background:var(--white);height:22px}
.hero--home .pager{left:203px;top:268px}
.hero--inner .pager{left:125px;top:170px}

/* home feature columns */
.features{position:absolute;left:130px;top:454px;width:831px;height:483px;display:flex}
.feature{width:277px;padding:0}
.feature--alt{background:var(--panel)}
.feature__photo{height:183px;background:linear-gradient(135deg,#e7e7e7,#9a9a9a 55%,#3a3a3a)}
.feature__body{padding:26px 16px 0 16px}
.feature h2{font-size:14px;color:var(--ink);line-height:17px;margin-bottom:24px}
.feature p{font-size:10px;line-height:13px;margin-bottom:13px}
.more{color:var(--brand);font-weight:700;font-size:10px}

.infoboxes{position:absolute;left:130px;top:937px;width:851px;height:261px;display:flex}
.infobox{width:283px;padding:34px 0 0 87px}
.infobox--grey{background:var(--panel)}
.infobox--firms{padding-left:87px}
.infobox h3{font-size:14px;color:var(--brand);font-weight:700;margin-left:-20px;margin-bottom:14px}
.firmlist{list-style:none}
.firmlist li{font-size:11px;font-weight:700;color:var(--ink);line-height:21px;position:relative;padding-left:10px}
.firmlist li::before,.sidenav li::before{content:"";position:absolute;left:0;top:7px;border-left:5px solid var(--brand);border-top:4px solid transparent;border-bottom:4px solid transparent}
.know{padding-left:82px}
.know h3{margin-left:0;margin-bottom:5px}
.know h4{font-size:11px;color:var(--ink);line-height:13px;margin-bottom:10px;width:110px}
.know p{font-size:9px;line-height:12px;width:110px}
.know a{color:var(--brand);font-weight:700}

/* inner content */
.article{position:absolute;left:125px;top:392px;width:643px}
.article h1{font-size:25px;color:var(--brand);font-weight:700;margin-bottom:22px}
.article h2{font-size:17px;color:var(--ink);font-weight:400;margin:16px 0 4px}
.article p{font-size:10.5px;line-height:13.5px;margin-bottom:13px}
.sidebar{position:absolute;left:801px;top:343px;width:141px}
.sidebox{background:var(--panel);padding:14px 10px}
.sidebox + .sidebox{margin-top:11px}
.sidenav{list-style:none}
.sidenav li{position:relative;padding-left:12px;font-size:11px;font-weight:700;color:var(--ink);line-height:21.4px}
.sidebox--nav{height:234px;padding-top:44px}
.sidebox--quote{height:235px}
.sidebox--news{height:364px;padding-top:22px}
.sidebox h5{font-size:10.5px;color:var(--ink);line-height:13px;margin-bottom:12px}
.sidebox p{font-size:10px;line-height:13px;color:var(--ink)}
.news-item{margin-bottom:14px;font-size:10px;line-height:13px;color:var(--ink)}
.news-item strong{display:block}
.news-item a{color:var(--brand)}

/* footer */
.sitemap{position:absolute;left:0;top:1201px;width:100%;height:295px;background:var(--footer);color:var(--footer-text)}
.sitemap__col{position:absolute;top:24px;font-size:11px;line-height:14px}
.sitemap__col h6{font-size:18px;color:var(--brand);margin-bottom:14px}
.subscribe{position:absolute;left:153px;top:184px}
.subscribe h6{font-size:11px;color:var(--white);margin-bottom:14px}
.subscribe__rss{display:flex;align-items:center;gap:9px;font-size:9.5px;color:#999}
.subscribe__rss b{color:var(--white);font-weight:400}
.rss-icon{width:22px;height:22px;border-radius:4px;background:var(--rss)}
.subscribe__form{display:flex;margin-top:12px}
.subscribe__input{width:158px;height:16px;background:var(--white);font-size:9px;color:#aaa;padding:2px 10px}
.subscribe__btn{width:20px;height:20px;background:var(--brand);margin-top:-2px}
.legal{position:absolute;left:385px;top:215px;display:flex;gap:17px;font-size:10px;color:var(--white)}
</style>
</head>
<body>

<section class="page page--home">
  <header class="masthead">
    <div class="brand"><span class="brand__dot"></span><span class="brand__name">Tolland Vesper</span></div>
  </header>
  <nav class="mainnav"><ul>
    <li class="is-current">Home</li>
    <li style="left:208px">About</li>
    <li style="left:278px">Services</li>
    <li style="left:365px">Our Network</li>
    <li style="left:480px">Infotelligence</li>
    <li style="left:607px">Contact</li>
    <li style="left:695px">Login</li>
    <li style="left:759px">Search</li>
  </ul></nav>

  <div class="hero hero--home">
    <h1 class="hero__title"><span class="hero__num">1.</span>Where to next?</h1>
    <p class="hero__lead">This is what we’re asked by many people and the reason why<br>our clients chose Tolland Vesper.</p>
    <p class="hero__body">Our clients know we are good at the fundamentals - accounting, tax compliance, and audit - but they come to us because we have the expertise to help them identify, structure, and secure their future... their next step.</p>
    <div class="hero__photo" role="img" aria-label="Businesswoman pointing towards the banner message"></div>
    <div class="pager"><span class="is-current">1</span><span>2</span><span>3</span><span>4</span><span>5</span></div>
  </div>

  <div class="features">
    <article class="feature">
      <div class="feature__photo" role="img" aria-label="Team meeting around a round table, viewed from above"></div>
      <div class="feature__body">
        <h2>The threat to businesses with unrelated shareholders</h2>
        <p>If you are in business with shareholders that are not related to you, your business faces a potentially major and costly threat, if one of your fellow shareholders dies or becomes permanently disabled.</p>
        <p>Good planning through buy/sell agreements and appropriate insurance can make all the difference.</p>
        <a class="more">Click here to find out more &gt;&gt;&gt;</a>
      </div>
    </article>
    <article class="feature feature--alt">
      <div class="feature__photo" role="img" aria-label="Presenter at a whiteboard in front of colleagues"></div>
      <div class="feature__body">
        <h2>Is good cash flow management enough to save your business?</h2>
        <p>A key issue introduction text goes here and links through to a webpage in the site. Can be a continuation of the article or a link to a general section of the site.</p>
        <p>It will not be more than 2 or 3 sentences to tease the visitor to click on the link.</p>
        <p>It must include much more white space (air) between the seperate pieces than this mockup actually shows.</p>
        <a class="more">Click here to find out more &gt;&gt;&gt;</a>
      </div>
    </article>
    <article class="feature">
      <div class="feature__photo" role="img" aria-label="Colleagues reviewing work at a laptop"></div>
      <div class="feature__body">
        <h2>Are you ready for Private Equity?</h2>
        <p>A key issue introduction text goes here and links through to a webpage in the site. Can be a continuation of the article or a link to a general section of the site.</p>
        <p>It will not be more than 2 or 3 sentences to tease the visitor to click on the link.</p>
        <p>It must include much more white space (air) between the seperate pieces than this mockup actually shows.</p>
        <a class="more">Click here to find out more &gt;&gt;&gt;</a>
      </div>
    </article>
  </div>

  <div class="infoboxes">
    <div class="infobox infobox--grey infobox--firms">
      <h3>Member Firms</h3>
      <ul class="firmlist">
        <li>Adelaide</li><li>Brisbane</li><li>Darwin</li><li>Perth</li><li>Sydney</li><li>Melbourne</li><li>New Zealand</li>
      </ul>
    </div>
    <div class="infobox know">
      <h3>In the Know...</h3>
      <h4>An ideaa to save you thousands!</h4>
      <p>The central bank has removed almost all of the mystery about what is going to happen with interest rates. Rates have bottomed out and are likely to start going up. <a>more&gt;&gt;&gt;</a></p>
    </div>
    <div class="infobox infobox--grey know">
      <h3>In the Know...</h3>
      <h4>Should I increase my prices?</h4>
      <p>The costs of running my business have gone up (despite what they keep telling me on the news) but I have held off increasing my prices. It just doesn't seem right when the economy... <a>more&gt;&gt;&gt;</a></p>
    </div>
  </div>

  <footer class="sitemap">
    <div class="sitemap__col" style="left:153px"><h6>About</h6>Innovative, Energetic, Streetsmart<br>Leadership team</div>
    <div class="sitemap__col" style="left:383px"><h6>Services</h6>Innovative, Energetic,<br>Leadership team<br>Innovative, Energetic<br>Innovative, Energetic<br>Energetic</div>
    <div class="sitemap__col" style="left:605px"><h6>Network</h6>Innovative<br>Energetic<br>Streetsmart<br>Leadership team</div>
    <div class="sitemap__col" style="left:818px"><h6>Knowledge</h6>Innovative, Energetic,<br>Streetsmart<br>Leadership team</div>
    <div class="subscribe">
      <h6>Subscribe</h6>
      <div class="subscribe__rss"><span class="rss-icon"></span>Subscribe via <b>RSS Feed Reader</b></div>
      <div class="subscribe__form"><span class="subscribe__input">e-mail adress</span><span class="subscribe__btn"></span></div>
    </div>
    <div class="legal"><span>Copyright</span><span>Privacy</span><span>Disclaimer</span><span>Subscribe</span><span>Site Manager</span><span>Links</span></div>
  </footer>
</section>

<section class="page page--inner">
  <header class="masthead">
    <div class="brand"><span class="brand__dot"></span><span class="brand__name">Tolland Vesper</span></div>
  </header>
  <nav class="mainnav"><ul>
    <li class="is-current">Home</li>
    <li style="left:208px">About</li>
    <li style="left:278px">Services</li>
    <li style="left:365px">Our Network</li>
    <li style="left:480px">Infotelligence</li>
    <li style="left:607px">Contact</li>
    <li style="left:695px">Login</li>
    <li style="left:759px">Search</li>
  </ul></nav>

  <div class="hero hero--inner">
    <h1 class="hero__title">Step <span class="hero__num">1</span></h1>
    <p class="hero__lead">Through our member firms, Tolland Vesper Employs and nurtures the intellectual capital<br>of over 600 talented and professional people across Australia and New Zealand.</p>
    <div class="pager"><span class="is-current">1</span><span>2</span><span>3</span><span>4</span></div>
  </div>

  <main class="article">
    <h1>Where to Next?</h1>
    <p>This is what we're asked by many people and the reason why our clients chose Tolland Vesper.</p>
    <p>Our clients know we are good at the fundamentals - accounting, tax compliance, and audit – but they come to us because not only are we good at the fundamentals, we have the expertise to help them identify, structure, and secure, their future…their next step.</p>
    <p>Whether you are a business owner or operator, or someone looking to seize the opportunities personally available to you, we can help.</p>
    <p>With a broad range of services and solutions, Tolland Vesper can help you achieve your next step.</p>
    <h2>Our structure</h2>
    <p>Tolland Vesper is an association (or federation?) of independent accounting firms across Australia and New Zealand (link). While we are united by a common culture and brand, each Tolland Vesper firm is independent. The team that run the firm, own the business and have a special interest in making sure that they deliver what clients need and an understanding of what it takes to succeed.</p>
    <h2>Our reach</h2>
    <p>Tolland Vesper is an independent member of Caldrew Global, a global association of 78 independent professional services firms covering accounting, audit, tax, business consulting and legal in 54 countries around the world.</p>
    <p>We know that nothing beats good local knowledge and representation to move things along and achieve the right results when you're operating across borders. Our connections through the Caldrew Global group are strong and ensure that, regardless of where you or your business need to go, we can offer you a professional and streamlined service.</p>
    <h2>Our history</h2>
    <p>Represented by eight firms across Australia and New Zealand with (?) directors and over (?) professional staff, the Tolland Vesper group is large enough to offer high level support and an impressive breadth of expertise, but small enough to give clients the individual attention they need.</p>
    <p>Like many businesses, our origins were small. Back in the early 1970s when flares were popular and the Kestrel/Harrow debate was in full swing, Glen Tolland started a one-man practice, GT Tolland &amp; Co, in the Sydney suburb of Campbelltown.</p>
    <p>A partnership, the adoption of the name Tolland Vesper, and a new office later, we decided to start practicing the strategies we were teaching our clients. Progressively, Tolland Vesper sought out like- minded professionals and in 1996, formed an association of independent accounting and business advisory firms.</p>
    <p>We know that a common culture and common goals are integral to success. All members of the Tolland Vesper group have been selected for their technical competency, professional success, 'real world' attitude and approach, client focus, and desire to achieve the right result.</p>
    <p>Bottom line; they're just good people to work with who take their work seriously but not themselves.</p>
  </main>

  <aside class="sidebar">
    <div class="sidebox sidebox--nav">
      <ul class="sidenav">
        <li>Contact</li><li>Structure</li><li>Creed</li><li>Member Firms</li><li>Leaders</li><li>Network</li><li>Community</li><li>News &amp; Events</li>
      </ul>
    </div>
    <div class="sidebox sidebox--quote">
      <h5>Don't take our word for it!</h5>
      <p>"Testimonial goes here... testimonial goes here and includes the persons and clients name. Sometimes will link through to a page, but not always. Client name will link to their website."<br>Person's name<br>Client name</p>
    </div>
    <div class="sidebox sidebox--news">
      <h5>Latest News &amp; Events</h5>
      <div class="news-item"><strong>Title link to article</strong>and short intro to the article <a>&gt;&gt;</a></div>
      <div class="news-item"><strong>Title link to article</strong>and short intro to the article <a>&gt;&gt;</a></div>
      <div class="news-item"><strong>Title link to article</strong>and short intro to the article <a>&gt;&gt;</a></div>
    </div>
  </aside>

  <footer class="sitemap">
    <div class="sitemap__col" style="left:153px"><h6>About</h6>Innovative, Energetic, Streetsmart<br>Leadership team</div>
    <div class="sitemap__col" style="left:383px"><h6>Services</h6>Innovative, Energetic,<br>Leadership team<br>Innovative, Energetic<br>Innovative, Energetic<br>Energetic</div>
    <div class="sitemap__col" style="left:605px"><h6>Network</h6>Innovative<br>Energetic<br>Streetsmart<br>Leadership team</div>
    <div class="sitemap__col" style="left:818px"><h6>Knowledge</h6>Innovative, Energetic,<br>Streetsmart<br>Leadership team</div>
    <div class="subscribe">
      <h6>Subscribe</h6>
      <div class="subscribe__rss"><span class="rss-icon"></span>Subscribe via <b>RSS Feed Reader</b></div>
      <div class="subscribe__form"><span class="subscribe__input">e-mail adress</span><span class="subscribe__btn"></span></div>
    </div>
    <div class="legal"><span>Copyright</span><span>Privacy</span><span>Disclaimer</span><span>Subscribe</span><span>Site Manager</span><span>Links</span></div>
  </footer>
</section>

</body>
</html>
```